K8 FIRST WEBSITE FOR CONCRETE DESIGN START-UP

We would like a 3-4 page website. Very basic. About Us, Pricing, Testimonials, Pictures and somewhere they can contact us. We are a concrete design/epoxy company. Want clean/modern and something that is user friendly that we can keep building on. Important we can update the website and that it shows good examples of our work.
Target Market(s)
Home owners or business owners who want unique solutions to concrete flooring in garages, patios, basements, showrooms or anywhere concrete is or can be.
Industry/Entity Type
Concrete
Coding
Coded - Design and coding required
Number of Pages Required
4 page

```html
<!DOCTYPE html>
<html lang="en">
<head>
<meta charset="utf-8">
<title>K8 Concrete</title>
<link href="https://fonts.googleapis.com/css2?family=Montserrat:wght@400;500;600;700;800&family=Quicksand:wght@400;500;600&display=swap" rel="stylesheet">
<style>
:root{
  --orange:#f15a29;
  --ink:#222;
  --muted:#777;
  --soft:#f6f6f6;
  --dark:#2b2b2b;
  --white:#fff;
}
*{box-sizing:border-box;margin:0;padding:0}
html,body{width:1200px;height:4000px;overflow:hidden;background:var(--white)}
body{position:relative;font-family:"Montserrat",sans-serif;color:var(--ink)}
.abs{position:absolute}

.hero{left:78px;top:26px;width:1047px;height:657px}
.hero-photo{left:0;top:0;width:1047px;height:657px;background:linear-gradient(180deg,#8e9294 0%,#c4c6c7 45%,#eeeeee 100%)}
.brand{left:86px;top:20px;font:800 20px "Montserrat",sans-serif;color:var(--white);letter-spacing:2px;display:flex;align-items:center;gap:8px}
.brand .mark{width:14px;height:14px;background:var(--orange)}
.nav{right:90px;top:24px;display:flex;gap:30px;font:500 12px "Montserrat",sans-serif;color:var(--white)}
.nav .active{color:var(--orange)}
.hero-name{left:0;width:1047px;top:220px;text-align:center;font:800 52px "Montserrat",sans-serif;color:#1c1c1c;letter-spacing:6px;display:flex;justify-content:center;align-items:center;gap:18px}
.hero-name .mark{width:34px;height:34px;background:var(--orange)}
.tagline{left:0;width:1047px;top:455px;text-align:center;font:600 13px "Montserrat",sans-serif;letter-spacing:1px;line-height:24px;color:#222}

.about-dots{left:514px;top:792px;width:44px;height:300px;background-image:radial-gradient(#bbb 1px,transparent 1.5px);background-size:22px 22px}
.about-copy{left:611px;top:784px;width:330px;font-size:11px;line-height:23px;color:#555}
.about-copy h3{font:500 11px "Montserrat",sans-serif;letter-spacing:1px;color:#555;margin-bottom:16px;line-height:23px}
.about-copy ul{list-style:disc;padding-left:30px;margin-bottom:16px}
.about-copy strong{color:var(--orange);font-weight:600}

.team{left:78px;top:1267px;width:807px;height:519px;background:var(--soft)}
.team-photo{left:627px;top:1357px;width:427px;height:302px;background:linear-gradient(135deg,#c9b89a 0%,#6f6a62 55%,#2f2d2a 100%);box-shadow:0 8px 24px rgba(0,0,0,.25)}
.team-dots{left:192px;top:1630px;width:32px;height:80px;background-image:radial-gradient(#bbb 1px,transparent 1.5px);background-size:16px 22px}
.team-copy{left:232px;top:1627px;width:340px;font-size:11px;line-height:23px;color:#555}

.testimonials{left:0;top:1900px;width:1200px;text-align:center}
.label{font:600 8px "Montserrat",sans-serif;letter-spacing:3px;color:#333}
.title{font:400 34px "Quicksand",sans-serif;color:#1c1c1c;margin-top:10px}
.title span{color:var(--orange)}
.quote{font:400 12px "Quicksand",sans-serif;color:#888;line-height:21px;margin-top:44px}
.person{font:600 13px "Montserrat",sans-serif;margin-top:28px}
.role{font:500 12px "Montserrat",sans-serif;color:var(--orange);margin-top:12px}
.date{font:500 8px "Montserrat",sans-serif;color:#555;margin-top:12px}
.dots{display:flex;justify-content:center;gap:10px;margin-top:18px}
.dots i{width:7px;height:7px;border-radius:50%;background:#666}
.dots i.on{background:var(--orange)}

.clients{left:78px;top:2297px;width:1047px;height:450px;background:var(--soft);text-align:center;padding-top:116px}
.client-row{display:flex;justify-content:center;margin-top:70px}
.client{width:216px;height:110px;border-right:1px solid #e8e8e8;display:flex;align-items:center;justify-content:center}
.client:last-child{border-right:none}
.client div{width:110px;height:48px;border:2px solid #a7a7a7;border-radius:4px}

.cta{left:78px;top:2747px;width:1047px;height:865px}
.cta-photo{left:0;top:0;width:1047px;height:865px;background:radial-gradient(circle at 50% 30%,#4a4a4a 0%,#2a2a2a 60%,#1e1e1e 100%)}
.cta-lead{left:0;width:1047px;top:110px;text-align:center;font:500 20px "Montserrat",sans-serif;color:#eee}
.cta-head{left:0;width:1047px;top:190px;text-align:center;font:800 33px "Montserrat",sans-serif;color:var(--orange);line-height:46px}
.contact{left:115px;top:362px;width:270px;color:#eee}
.contact .label{color:#eee}
.contact h2{font:400 34px "Quicksand",sans-serif;line-height:46px;margin-top:28px}
.contact p{font:400 12px "Quicksand",sans-serif;line-height:21px;margin-top:20px}
.cta-brand{left:125px;top:650px;font:800 24px "Montserrat",sans-serif;color:var(--white);letter-spacing:3px;display:flex;align-items:center;gap:10px}
.cta-brand .mark{width:20px;height:20px;background:var(--orange)}
.form{left:442px;top:345px;width:505px}
.form label{display:block;font:400 11px "Montserrat",sans-serif;color:#bbb;height:16px}
.form .field{height:32px;border:1px solid #888;margin-bottom:19px}
.form .area{height:124px;border:1px solid #888;margin-bottom:15px}
.form .send{width:114px;height:41px;background:var(--white);color:#222;font:600 11px "Montserrat",sans-serif;letter-spacing:1px;display:flex;align-items:center;justify-content:center}
</style>
</head>
<body>

<header class="abs hero">
  <div class="abs hero-photo" role="img" aria-label="Photo of a white hard hat in an empty concrete warehouse"></div>
  <div class="abs brand"><span class="mark"></span>K8 CONCRETE</div>
  <nav class="abs nav"><span class="active">Home</span><span>About Us</span><span>Testimonials</span><span>Pricing</span><span>Contact us</span></nav>
  <div class="abs hero-name"><span class="mark"></span>K8 CONCRETE</div>
  <p class="abs tagline">FLOORING IN GARAGES, PATIOS, BASEMENTS, SHOWROOMS OR<br>ANYWHERE CONCRETE IS OR CAN BE</p>
</header>

<section>
  <div class="abs about-dots"></div>
  <div class="abs about-copy">
    <h3>PERFECT INTALLATIONS &amp; OUTSTANDING CUSTOMER SERVICE</h3>
    <ul>
      <li>Annually Trained and Certified Installers</li>
      <li>Innovative Designs</li>
      <li>Highest Quality Products</li>
      <li>Excellent Customer Service</li>
    </ul>
    <p>In choosing <strong>K8 Concrete</strong> for your decorative concrete resurfacing needs, you will receive a one of a kind service experience. We will work with you one on one to understand your vision and turn it into a reality. Contact us to schedule an in-depth consultation at your home or business which you will learn more about our flooring systems and technical application process. After we have assessed your needs, we will step you through the transformation process and keep you well informed throughout the entirety of your project.</p>
  </div>
</section>

<section>
  <div class="abs team"></div>
  <div class="abs team-photo" role="img" aria-label="Photo of a concrete floor grinding machine at work"></div>
  <div class="abs team-dots"></div>
  <p class="abs team-copy">The team takes immense pride not only in the creative and work we produce, but also service. We love great design and thrive on the enthusiasm of the businesses we work with on a daily basis.</p>
</section>

<section class="abs testimonials">
  <div class="label">TESTIMONIALS</div>
  <h2 class="title">What they say <span>about us</span></h2>
  <p class="quote">Lorem ipsum dolor sit amet, consectetur adipiscing elit, sed do<br>eiusmod tempor incididunt ut labore et dolore magna aliqua.</p>
  <div class="person">Dana Whitlow</div>
  <div class="role">Founder &amp; CEO</div>
  <div class="date">Thursday, August 31, 2017</div>
  <div class="dots"><i></i><i></i><i></i><i class="on"></i></div>
</section>

<section class="abs clients">
  <div class="label">OUR CLIENTS AND PARTNERS</div>
  <h2 class="title">Happy clients</h2>
  <div class="client-row">
    <div class="client"><div></div></div>
    <div class="client"><div></div></div>
    <div class="client"><div></div></div>
    <div class="client"><div></div></div>
  </div>
</section>

<section class="abs cta">
  <div class="abs cta-photo" role="img" aria-label="Dark photo of a polished terrazzo floor in a modern lounge"></div>
  <p class="abs cta-lead">OUR FLOORING APPLICATIONS HAVE ENDLESS POSSIBILITIES.</p>
  <h2 class="abs cta-head">OUR TEAM OF EXPERTS WILL WALK YOU THROUGH THE<br>PROCESS OF TRANSFORMING YOU CONCRETE.</h2>
  <div class="abs contact">
    <div class="label">CONTACT US NOW</div>
    <h2>Request<br>a call back</h2>
    <p>Whatever types of questions you'll have,<br>feel free to get in touch with us!</p>
  </div>
  <div class="abs cta-brand"><span class="mark"></span>K8 CONCRETE</div>
  <form class="abs form">
    <label>Your Name (required)</label><div class="field"></div>
    <label>Your Email (required)</label><div class="field"></div>
    <label>Subject</label><div class="field"></div>
    <label>Your Message</label><div class="area"></div>
    <div class="send">SEND</div>
  </form>
</section>

</body>
</html>
```